IT Professional business card with a hometown feel and a little edgy.

My business name is Pebble Website Solutions. But I have ended up doing much more. I live in a very small remote community, where everyone knows everyone. We like the one-on-one customer service in this community. I do computer tutoring, virus removal, networking, and software training. My clients are businesses and private individuals.

My website is pebblewebsitesolutions.example, when I first designed it I was going for a fresh, clean look, which I still like. But I am thinking about making the website a bit more edgy to match my new logo from ArtGrovely (logo attached). At this time my website does not display the new logo, but I plan on redesigning the website in the future to match the logo and business card.

My tag line is "Put the web on your side"

I'm thinking I would like to have the business card printed with a metallic finish.

Please do not use black backgrounds, or any solid dark colors. Prefer light or white backgrounds.

Target Market(s)

Small businesses. Individuals that need computer help at home.

Industry/Entity Type

It Company

Contact Information for Business Card

Marla Dunovan
Pebble Website Solutions
PO Box 7153
Alderwick, WA 98590
Cell: 360-555-0172
marla@pebblewebsitesolutions.example
pebblewebsitesolutions.example

Font styles to use
Serif

Requirements
Must have
• Must have all the information listed in "Business Card Details"
• Must use the logo provided.
• Use the colors from the provided logo
Nice to have
• Would like to use my tagline "Put the web on your side" all lowercase

```html
<!DOCTYPE html>
<html lang="en">
<head>
<meta charset="utf-8">
<title>Pebble Website Solutions — Business Card</title>
<link rel="stylesheet" href="https://fonts.googleapis.com/css2?family=Roboto+Slab:wght@400;700&family=Montserrat:wght@800&display=swap">
<style>
  :root {
    --page: #ecefea;
    --green-deep: #1b5e27;
    --green-mid: #2e8a3c;
    --green-light: #8fd66a;
    --green-pale: #b4e88e;
    --green-tag: #5cb82e;
    --green-dark-text: #24632d;
    --white: #ffffff;
    --shadow: rgba(20, 40, 20, 0.22);
  }
  * { box-sizing: border-box; margin: 0; padding: 0; }
  html, body {
    width: 1200px; height: 913px; overflow: hidden;
    background: var(--page);
  }
  .canvas { position: relative; width: 1200px; height: 913px; }
  .card {
    position: absolute; width: 525px; height: 300px;
    border-radius: 18px; overflow: hidden;
    box-shadow: 0 10px 28px var(--shadow);
  }
  .card-front {
    left: 55px; top: 150px;
    background: linear-gradient(135deg, var(--green-deep) 0%, var(--green-mid) 70%);
  }
  .front-swoosh { position: absolute; inset: 0; }
  .brand {
    position: absolute; left: 32px; top: 44px;
    display: flex; align-items: center; gap: 12px;
  }
  .brand-square {
    width: 34px; height: 34px; border: 4px solid var(--green-light); flex: none;
  }
  .brand-name {
    font-family: "Roboto Slab", serif; font-weight: 400;
    font-size: 18px; color: var(--green-pale); letter-spacing: 0.3px;
    white-space: nowrap;
  }
  .contact-strip {
    position: absolute; left: 0; bottom: 26px;
    width: 22px; height: 88px; background: var(--white);
  }
  .contact {
    position: absolute; left: 38px; bottom: 22px;
    font-family: "Roboto Slab", serif; color: var(--white);
  }
  .contact-name { font-weight: 700; font-size: 22px; margin-bottom: 6px; }
  .contact-line {
    display: flex; align-items: center; gap: 8px;
    font-size: 13px; line-height: 21px; white-space: nowrap;
  }
  .contact-line svg { width: 13px; height: 13px; flex: none; }
  .contact-line .no-icon { width: 13px; flex: none; }
  .card-back {
    left: 620px; top: 470px; background: var(--white);
  }
  .back-brand {
    position: absolute; left: 0; right: 0; top: 92px;
    display: flex; justify-content: center; align-items: center; gap: 16px;
  }
  .back-brand .brand-square { width: 52px; height: 52px; border-width: 6px; border-color: var(--green-mid); }
  .back-brand .brand-name { font-size: 28px; color: var(--green-deep); }
  .tagline {
    position: absolute; left: 0; right: 0; bottom: 58px; text-align: center;
    font-family: "Montserrat", sans-serif; font-weight: 800;
    font-size: 19px; letter-spacing: 0.5px; color: var(--green-dark-text);
  }
  .tagline .accent { color: var(--green-tag); }
</style>
</head>
<body>
<main class="canvas">
  <section class="card card-front" aria-label="Business card front">
    <svg class="front-swoosh" viewBox="0 0 525 300" preserveAspectRatio="none" aria-hidden="true">
      <defs>
        <linearGradient id="swooshFill" x1="0" y1="0" x2="1" y2="1">
          <stop offset="0" stop-color="#c2ef9c"/>
          <stop offset="1" stop-color="#6cc24a"/>
        </linearGradient>
      </defs>
      <path d="M330 0 C300 60 420 110 410 200 C405 250 380 290 372 300 L525 300 L525 0 Z" fill="url(#swooshFill)"/>
      <path d="M395 70 C450 110 470 190 410 300 L430 300 C480 200 470 120 395 70 Z" fill="#7fd05a"/>
    </svg>
    <div class="brand">
      <span class="brand-square" aria-hidden="true"></span>
      <span class="brand-name">Pebble Website Solutions</span>
    </div>
    <div class="contact-strip" aria-hidden="true"></div>
    <div class="contact">
      <p class="contact-name">Marla Dunovan</p>
      <p class="contact-line"><span class="no-icon"></span>PO Box 7153 Alderwick, WA 98590</p>
      <p class="contact-line">
        <svg viewBox="0 0 12 12" aria-hidden="true"><rect x="3" y="0.5" width="6" height="11" rx="1" fill="none" stroke="#fff"/><line x1="5" y1="10" x2="7" y2="10" stroke="#fff"/></svg>
        360-555-0172</p>
      <p class="contact-line">
        <svg viewBox="0 0 12 12" aria-hidden="true"><rect x="0.5" y="2.5" width="11" height="7" fill="none" stroke="#fff"/><path d="M0.5 2.5 L6 7 L11.5 2.5" fill="none" stroke="#fff"/></svg>
        marla@pebblewebsitesolutions.example</p>
      <p class="contact-line">
        <svg viewBox="0 0 12 12" aria-hidden="true"><circle cx="6" cy="6" r="5.5" fill="none" stroke="#fff"/><ellipse cx="6" cy="6" rx="2.3" ry="5.5" fill="none" stroke="#fff"/><line x1="0.5" y1="6" x2="11.5" y2="6" stroke="#fff"/></svg>
        www.pebblewebsitesolutions.example</p>
    </div>
  </section>

  <section class="card card-back" aria-label="Business card back">
    <div class="back-brand">
      <span class="brand-square" aria-hidden="true"></span>
      <span class="brand-name">Pebble Website Solutions</span>
    </div>
    <p class="tagline">PUT THE WEB <span class="accent">ON YOUR SIDE</span></p>
  </section>
</main>
</body>
</html>
```